Business card design needed

We need a double sided business card for an established business which currently installs, repairs, services & inspects truck mounted elevated work platforms and are looking to branch out our auto electrical department. We would like a black business card featuring some sort of auto electrical graphic (not cars) eg. wires, fuses etc. and keeping with our theme of black and orange. Also stipulating that we are heavy fleet specialists.

Industry/Entity Type

Electrical

Contact Information for Business Card

Marcel Hobbs
Auto Electrical Supervisor
27 Tanager Crescent, Currumbin Q 4223
(PO Box 817, Currumbin Q 4223)
p 07 5611 7089
f 07 5611 7090
m 0491 735284
e info@brantelgroup.com.au

Requirements
Must have
• the business card must incorporate the logos attached. the QMS4417 and the CRB-PTV logo MUST be of the same size and be situated together with QMS4417 on the left side and CRB-PTV on the right.
heavy fleet specialist
sales
service
spare parts
inspections
repairs
maintenance
new installations
Should not have
• images of cars or trucks, old style fonts

```html
<!DOCTYPE html>
<html lang="en">
<head>
<meta charset="utf-8">
<title>Brantel Group – Business Card</title>
<link rel="stylesheet" href="https://fonts.googleapis.com/css2?family=Exo+2:wght@400;600;700&display=swap">
<style>
  :root {
    --bg: #b9b9b7;
    --card: #0b0a09;
    --card-glow: #24170b;
    --orange: #f08a1c;
    --orange-deep: #c9640c;
    --orange-soft: rgba(240,138,28,0.34);
    --orange-faint: rgba(201,100,12,0.06);
    --grey-text: #c9c9c9;
    --badge-red: #d8262e;
    --badge-blue: #1f4fa1;
  }
  * { box-sizing: border-box; margin: 0; padding: 0; }
  html, body { width: 1200px; height: 799px; overflow: hidden; }
  body {
    background: var(--bg);
    font-family: "Exo 2", sans-serif;
    display: flex;
    align-items: center;
    justify-content: center;
    gap: 36px;
  }
  .card {
    position: relative;
    width: 546px;
    height: 312px;
    background: radial-gradient(ellipse at 62% 45%, var(--card-glow) 0%, var(--card) 62%);
    overflow: hidden;
    color: var(--orange);
  }
  .circuit-art {
    position: absolute;
    background:
      radial-gradient(ellipse at 30% 50%, var(--orange-soft), transparent 70%),
      linear-gradient(100deg, var(--orange-faint), transparent);
  }
  .rule {
    position: absolute;
    height: 3px;
    background: linear-gradient(90deg, var(--orange-deep), var(--orange), #ffd27a 75%, var(--orange));
  }
  .brand {
    position: absolute;
    font-weight: 700;
    color: var(--orange);
    letter-spacing: 2px;
    display: flex;
    align-items: center;
    gap: 8px;
    z-index: 1;
  }
  .brand-mark { width: 12px; height: 12px; background: var(--orange); }

  /* services side */
  .card--services .circuit-art--top { top: 0; left: 0; right: 0; height: 110px; }
  .card--services .circuit-art--side { top: 118px; right: 0; width: 200px; height: 70px; }
  .card--services .brand { top: 40px; left: 150px; font-size: 32px; }
  .card--services .rule--top { top: 112px; left: 0; right: 0; }
  .card--services .rule--bottom { top: 268px; left: 0; right: 0; }
  .service-list {
    position: absolute;
    top: 134px; left: 26px;
    font-size: 15px;
    line-height: 26px;
    color: var(--grey-text);
    letter-spacing: 1.5px;
    text-transform: uppercase;
  }
  .service-list .sep { color: var(--orange); margin: 0 6px; }
  .badges {
    position: absolute;
    right: 26px; top: 196px;
    display: flex; gap: 12px;
  }
  .badge { width: 46px; height: 54px; }
  .badge--quality { background: var(--badge-red); }
  .badge--accreditation { background: var(--badge-blue); }

  /* contact side */
  .card--contact .brand { top: 26px; left: 26px; font-size: 24px; }
  .card--contact .circuit-art { top: 66px; left: 0; width: 320px; height: 124px; }
  .card--contact .rule--mid { top: 192px; left: 0; right: 0; }
  .specialist-tag {
    position: absolute;
    top: 82px; right: 36px;
    border: 2px solid var(--orange);
    padding: 2px 14px;
    font-weight: 700;
    font-size: 17px;
  }
  .person { position: absolute; top: 128px; right: 42px; }
  .person-name { font-size: 28px; font-weight: 700; line-height: 1; }
  .person-role { font-size: 14px; margin-top: 4px; }
  .address {
    position: absolute;
    top: 210px; left: 26px;
    display: flex; gap: 12px;
    font-size: 12px; line-height: 17px;
  }
  .address-icons { display: flex; flex-direction: column; gap: 4px; padding-top: 2px; }
  .extra-contacts {
    position: absolute;
    top: 240px; left: 300px;
    font-size: 13px;
    display: flex; flex-direction: column; gap: 8px;
  }
  .extra-contacts li { list-style: none; display: flex; align-items: center; gap: 12px; }
</style>
</head>
<body>

  <section class="card card--services" aria-label="Business card, services side">
    <div class="circuit-art circuit-art--top" role="img" aria-label="Orange circuit-board wiring traces (auto electrical graphic)"></div>
    <div class="circuit-art circuit-art--side" role="img" aria-label="Orange circuit-board wiring traces continuing at right"></div>
    <div class="brand"><span class="brand-mark"></span>BRANTEL GROUP</div>
    <div class="rule rule--top"></div>
    <p class="service-list">
      <span class="sep">|</span>Heavy Fleet Specialist<span class="sep">|</span>Sales<span class="sep">|</span>Service<span class="sep">|</span><br>
      <span class="sep">|</span>Spare Parts<span class="sep">|</span>Inspections<span class="sep">|</span>Repairs<span class="sep">|</span><br>
      <span class="sep">|</span>Maintenance<span class="sep">|</span>New Installations<span class="sep">|</span>
    </p>
    <div class="badges">
      <div class="badge badge--quality" role="img" aria-label="QMS4417 certification badge"></div>
      <div class="badge badge--accreditation" role="img" aria-label="CRB-PTV accreditation badge"></div>
    </div>
    <div class="rule rule--bottom"></div>
  </section>

  <section class="card card--contact" aria-label="Business card, contact side">
    <div class="brand"><span class="brand-mark"></span>BRANTEL GROUP</div>
    <div class="circuit-art" role="img" aria-label="Orange circuit-board wiring traces (auto electrical graphic)"></div>
    <div class="specialist-tag">Heavy Fleet Specialists</div>
    <div class="person">
      <p class="person-name">Marcel Hobbs</p>
      <p class="person-role">Auto Electrical Supervisor</p>
    </div>
    <div class="rule rule--mid"></div>
    <div class="address">
      <div class="address-icons">
        <svg width="14" height="14" viewBox="0 0 14 14" aria-hidden="true"><path d="M3 1h3l1 3-2 1a7 7 0 0 0 4 4l1-2 3 1v3a2 2 0 0 1-2 2A11 11 0 0 1 1 3a2 2 0 0 1 2-2z" fill="none" stroke="#f08a1c" stroke-width="1.2"/></svg>
        <svg width="14" height="14" viewBox="0 0 14 14" aria-hidden="true"><rect x="3" y="1" width="8" height="12" rx="2" fill="none" stroke="#f08a1c" stroke-width="1.2"/><line x1="6" y1="11" x2="8" y2="11" stroke="#f08a1c"/></svg>
      </div>
      <div>
        <p>27 Tanager Crescent, Currumbin Q 4223</p>
        <p>(PO Box 817, Currumbin Q 4223)</p>
        <p>07 5611 7089</p>
        <p>0491 735284</p>
      </div>
    </div>
    <ul class="extra-contacts">
      <li><svg width="18" height="14" viewBox="0 0 18 14" aria-hidden="true"><rect x="1" y="5" width="16" height="8" fill="none" stroke="#f08a1c" stroke-width="1.2"/><rect x="4" y="1" width="10" height="4" fill="none" stroke="#f08a1c" stroke-width="1.2"/></svg>07 5611 7090</li>
      <li><svg width="18" height="14" viewBox="0 0 18 14" aria-hidden="true"><rect x="1" y="1" width="16" height="12" fill="none" stroke="#f08a1c" stroke-width="1.2"/><path d="M1 1l8 7 8-7" fill="none" stroke="#f08a1c" stroke-width="1.2"/></svg>info@brantelgroup.com.au</li>
    </ul>
  </section>

</body>
</html>
```